My company is all about art and painting people's walls, cars and everything you can imagine, I would like a sharp professional buisness card which still has a good creative element

Industry/Entity Type

Painting

Contact Information for Business Card

Ve Rubel Art
Canvass,Murals,Vehicles,Cover art and tattoo design
Commissions available..
Www.brightwall.example/tavmiu

```html
<!DOCTYPE html>
<html lang="en">
<head>
<meta charset="utf-8">
<title>Ve Rubel Arts – Business Card</title>
<link rel="stylesheet" href="https://fonts.googleapis.com/css2?family=Source+Sans+3:wght@400&family=Open+Sans:wght@700&display=swap">
<style>
  :root {
    --orange: #d68a45;
    --yellow: #d6bc4a;
    --lime: #b3bc5a;
    --teal: #5eab90;
    --blue: #5c9daa;
    --purple: #9470a6;
    --red: #c44f5a;
    --ink: #ffffff;
    --stripe: 86.5px;
  }
  html, body {
    margin: 0;
    padding: 0;
    width: 1200px;
    height: 741px;
    overflow: hidden;
  }
  .card {
    position: relative;
    width: 1200px;
    height: 741px;
    overflow: hidden;
    background: repeating-linear-gradient(
      90deg,
      var(--orange) 0 calc(var(--stripe) * 1),
      var(--yellow) calc(var(--stripe) * 1) calc(var(--stripe) * 2),
      var(--lime) calc(var(--stripe) * 2) calc(var(--stripe) * 3),
      var(--teal) calc(var(--stripe) * 3) calc(var(--stripe) * 4),
      var(--blue) calc(var(--stripe) * 4) calc(var(--stripe) * 5),
      var(--purple) calc(var(--stripe) * 5) calc(var(--stripe) * 6),
      var(--red) calc(var(--stripe) * 6) calc(var(--stripe) * 7)
    );
    color: var(--ink);
  }
  .card__name {
    position: absolute;
    left: 40px;
    right: 40px;
    top: 216px;
    margin: 0;
    text-align: center;
    font-family: "Source Sans 3", sans-serif;
    font-weight: 400;
    font-size: 198px;
    line-height: 1;
    letter-spacing: -3px;
    white-space: nowrap;
  }
  .card__services {
    position: absolute;
    left: 95px;
    width: 900px;
    top: 424px;
    margin: 0;
    text-align: center;
    font-family: "Open Sans", sans-serif;
    font-weight: 700;
    font-size: 44px;
    line-height: 51px;
    letter-spacing: -0.5px;
  }
  .card__web {
    position: absolute;
    right: 28px;
    top: 658px;
    margin: 0;
    font-family: "Open Sans", sans-serif;
    font-weight: 700;
    font-size: 32px;
    line-height: 1;
    letter-spacing: -0.3px;
  }
</style>
</head>
<body>
  <main class="card">
    <h1 class="card__name">Ve Rubel Arts</h1>
    <p class="card__services">Canvass,Murals,Vehicles,Cover art<br>&amp; tattoo design Commissions<br>available</p>
    <p class="card__web">www.brightwall.example/tavmiu</p>
  </main>
</body>
</html>
```